Bluewater Motor Finance Home Page

We need a desktop version mock up (we will base our mobile version off of this) of a website homepage for our auto loan business, Bluewater Motor Finance. This does not need to be a functioning site, just a home page mock up. We are based in the metro St. Louis, MO area. We offer "guaranteed" auto loans for all credit types. We specialize in financing for bad/no credit customers. We are able to help rebuild these type of customers' credit, all while putting them in a great late model vehicle they'll love. Our online credit app takes less than 60 seconds, doesn't require a SS# and gives a free credit score if they fill it out within 3 minutes. We are looking for an outside perspective to help us in this design process. We are not completely sure what we want, but we do want it to be professional and secure looking, all while being unique and aesthetically pleasing. We want the customer to be able to put in their zip code to be directed to the right location that can get them pre approved. I attached a wireframe with some stuff we'd like to include, but in no way does it have to be in the same layout or the same ideas. We want everyone to "go crazy" with their creative side on this. Our current site is awful, here is a link to get a better idea: www.bluewatermotorfinance-example.com. Attached is our logo too, base colors off of it. Watch our video that is also attached for a better idea.

Target Market(s)

Residents of the St. Louis Missouri Metro Area that need an auto loan. 24-55 Male and Female - Lots of "urban market" customers.

Industry/Entity Type

Loan

Number of Pages Required

1 page

Colors
9bcb3b

Requirements
Must have
• An area where the customer can enter their zip code - Be creative!
Nice to have
• See wireframe attachment for ideas - Be creative!

```html
<!DOCTYPE html>
<html lang="en">
<head>
<meta charset="utf-8">
<title>Bluewater Motor Finance – Home</title>
<link href="https://fonts.googleapis.com/css2?family=Ropa+Sans&family=Roboto:wght@400;500&family=Libre+Baskerville:ital@1&display=swap" rel="stylesheet">
<style>
  :root{
    --page-bg:#eeeeee;
    --nav-bg:#2a2a2a;
    --nav-text:#ffffff;
    --nav-active:#9a9a9a;
    --brand-green:#9bc43c;
    --logo-green:#3cb43c;
    --headline-yellow:#f5d800;
    --button-yellow:#ffd600;
    --button-text:#2e6f9a;
    --panel-tint:rgba(125,195,235,0.55);
    --panel-edge:rgba(200,235,255,0.6);
    --form-blue:#3399cc;
    --form-edge:#6cc0e6;
    --white:#ffffff;
    --placeholder:#b5b5b5;
    --timer-text:#222222;
  }
  *{box-sizing:border-box;margin:0;padding:0}
  html,body{width:1200px;height:1000px;overflow:hidden;background:var(--page-bg)}
  body{font-family:"Roboto",Arial,sans-serif;position:relative}

  .site{position:absolute;left:0;top:173px;width:1200px;height:654px;overflow:hidden}

  /* Header */
  .site-header{position:absolute;left:0;top:0;width:1200px;height:94px;background:var(--nav-bg)}
  .brand{position:absolute;left:115px;top:22px;width:230px;height:50px;display:flex;align-items:center;gap:10px}
  .brand-mark{flex:none;width:38px;height:38px;background:var(--logo-green)}
  .brand-name{font-family:"Ropa Sans",Arial,sans-serif;font-size:22px;line-height:23px;color:var(--logo-green)}
  .nav-tab-active{position:absolute;left:365px;top:0;width:114px;height:94px;background:var(--nav-active);border-bottom:7px solid var(--brand-green)}
  .nav-item{position:absolute;top:47px;transform:translate(-50%,-50%);color:var(--nav-text);font-size:16px;white-space:nowrap}

  /* Hero */
  .hero{position:absolute;left:0;top:94px;width:1200px;height:458px}
  .hero-photo{position:absolute;inset:0;background:linear-gradient(100deg,#3b4a5e 0%,#6d8aa6 30%,#a9c4da 55%,#c8d6e0 75%,#8b97a3 100%)}
  .hero-panel{position:absolute;left:151px;top:74px;width:939px;height:300px;background:var(--panel-tint);border:1px solid var(--panel-edge)}
  .hero-title{position:absolute;left:0;top:24px;width:100%;text-align:center;font-family:"Ropa Sans",Arial,sans-serif;font-weight:400;font-size:62px;line-height:66px;color:var(--headline-yellow)}
  .hero-subtitle{position:absolute;left:0;top:88px;width:100%;text-align:center;font-family:"Libre Baskerville",Georgia,serif;font-style:italic;font-size:24px;color:var(--white)}

  .zip-form{position:absolute;left:30px;top:150px;width:541px;height:126px;background:var(--form-blue);border:1px solid var(--form-edge);border-radius:5px}
  .zip-input{position:absolute;left:27px;top:45px;width:218px;height:36px;background:var(--white);border:1px solid #d0d0d0;color:var(--placeholder);font-size:15px;line-height:34px;padding-left:10px}
  .zip-submit{position:absolute;left:292px;top:45px;width:218px;height:36px;background:var(--button-yellow);color:var(--button-text);font-size:16px;line-height:36px;text-align:center}

  .benefits{position:absolute;left:593px;top:162px;list-style:none}
  .benefits li{display:flex;align-items:center;gap:16px;height:29px;color:var(--white);font-size:19px;white-space:nowrap}
  .benefits li::before{content:"";flex:none;width:15px;height:15px;background:var(--white);border-radius:2px}

  /* Credit score band */
  .score-band{position:absolute;left:0;top:552px;width:1200px;height:102px;background:var(--brand-green);display:flex;align-items:center;justify-content:center;gap:24px;color:var(--white);font-size:25px}
  .timer{width:116px;height:51px;background:var(--white);color:var(--timer-text);border-radius:3px;display:flex;align-items:center;justify-content:center;font-size:25px}
</style>
</head>
<body>
  <main class="site">
    <header class="site-header">
      <div class="brand"><span class="brand-mark"></span><span class="brand-name">Bluewater Motor<br>Finance</span></div>
      <div class="nav-tab-active"></div>
      <span class="nav-item" style="left:422px">Locations</span>
      <span class="nav-item" style="left:566px">Finance Center</span>
      <span class="nav-item" style="left:692px">About</span>
      <span class="nav-item" style="left:781px">FAQ</span>
      <span class="nav-item" style="left:870px">Contact</span>
      <span class="nav-item" style="left:1024px">CALL (800) 555-0142</span>
    </header>

    <section class="hero">
      <div class="hero-photo" role="img" aria-label="Photo of a hand holding out car keys in front of a dealership lot with parked cars"></div>
      <div class="hero-panel">
        <h1 class="hero-title">Over 30,000 Auto Loans Since 2000</h1>
        <p class="hero-subtitle">Pre-Approval in Under 60 Seconds!</p>
        <div class="zip-form">
          <div class="zip-input">Enter your zip code</div>
          <div class="zip-submit">Get Approved</div>
        </div>
        <ul class="benefits">
          <li>No Social Security Number Required</li>
          <li>Instant Approval</li>
          <li>No Application Fees</li>
          <li>All Credit Accepted</li>
        </ul>
      </div>
    </section>

    <section class="score-band">
      <span>Apply within</span>
      <span class="timer">3:00</span>
      <span>and see your credit score for free!</span>
    </section>
  </main>
</body>
</html>
```